Landing Page IT Security Vendor

We need a landing page that uses our colour scheme (www.veldonguard.com). We created a draft (see attached). We do not need standard stock template design pages. Please only apply if you can design pages from scratch and try to be as close as possible to our draft. It is ok to also purchase commecrial stock pictures

Coding

Coded - Design and coding required

Number of Pages Required

1 page

```html
<!DOCTYPE html>
<html lang="en">
<head>
<meta charset="utf-8">
<title>Veldon Guard – Security Awareness</title>
<link rel="stylesheet" href="https://fonts.googleapis.com/css2?family=Open+Sans:wght@400;600;700&family=Roboto+Condensed:wght@400;700&display=swap">
<style>
:root{
  --teal:#00a8b2;
  --teal-dark:#007a80;
  --teal-deep:#06656b;
  --orange:#f9a51a;
  --orange-soft:#fbb03b;
  --ink:#222;
  --muted:#666;
  --card:#f7f7f7;
  --white:#fff;
  --sky:#4fb3f0;
}
*{box-sizing:border-box;margin:0;padding:0}
html,body{width:1200px;height:2400px;overflow:hidden;background:var(--white)}
body{position:relative;font-family:"Open Sans",Arial,sans-serif;color:var(--ink)}
.abs{position:absolute}
.bg-art{position:absolute;left:0;top:0}
.award{font-size:9.5px;line-height:15px;color:var(--white)}
.nav-btn{font-size:10px;color:var(--white);display:flex;align-items:center;justify-content:center}
.nav-home{border:1px solid var(--white)}
.nav-solution{background:var(--orange)}
.hero-line{right:40px;text-align:right;color:var(--white);font-size:19px;line-height:28px;letter-spacing:.2px}
.demo-btn{left:908px;top:263px;width:171px;height:48px;background:var(--teal-dark);border-radius:4px;color:var(--white);font-size:12.5px;display:flex;align-items:center;justify-content:center}
.art{position:absolute}
.ribbon-area{left:240px;top:580px;width:960px;height:440px;background:linear-gradient(160deg,rgba(79,179,240,0) 20%,rgba(79,179,240,.18) 55%,rgba(79,179,240,0) 85%)}
.dot{position:absolute;border-radius:50%}
.help-box{left:854px;top:500px;width:346px;height:76px;background:linear-gradient(90deg,var(--teal-deep),var(--teal));color:var(--white);font-weight:700;font-size:29px;letter-spacing:.5px;display:flex;align-items:center;padding-left:21px;white-space:nowrap}
.card{position:absolute;width:333px;background:var(--card);box-shadow:0 2px 6px rgba(0,0,0,.15)}
.card-head{height:49px;background:linear-gradient(90deg,var(--teal-dark),var(--teal));color:var(--white);font-weight:700;font-size:14px;line-height:17px;display:flex;flex-direction:column;justify-content:center;text-align:center;white-space:nowrap}
.card-head.left{text-align:left;padding-left:16px;font-size:12.8px;letter-spacing:-.1px}
.card-lead{margin:25px 34px 0 38px;font-weight:600;font-size:12px;line-height:17px;color:var(--ink)}
.card-text{margin:32px 34px 0 38px;font-size:10.5px;line-height:17px;color:var(--muted);font-weight:600}
.card-btn{position:absolute;left:43px;width:248px;height:52px;background:var(--orange);border-radius:3px;color:var(--white);font-weight:700;font-size:14px;display:flex;align-items:center;justify-content:center}
.mssp{left:0;top:1199px;width:590px;height:76px;background:linear-gradient(90deg,var(--teal-deep),var(--teal));color:var(--white);font-weight:700;font-size:26px;display:flex;align-items:center;padding-left:14px;white-space:nowrap}
.learn{left:614px;top:1222px;width:97px;height:31px;border:2px solid var(--teal-dark);border-radius:4px;color:#777;font-size:13px;display:flex;align-items:center;justify-content:center}
.trust-line{left:61px;color:var(--white);font-size:25px;line-height:34px;white-space:nowrap}
.contact-btn{left:199px;top:1703px;width:349px;height:52px;background:var(--orange-soft);border-radius:3px;color:var(--white);font-weight:700;font-size:14px;display:flex;align-items:center;justify-content:center}
.clients{left:36px;top:1836px;width:1128px;height:152px;display:flex;align-items:center;justify-content:space-between}
.client{display:flex;align-items:center;gap:10px;font-weight:700;font-size:30px;color:var(--teal-deep)}
.client .mark{width:22px;height:22px;background:var(--teal)}
.footer{left:0;top:2022px;width:1200px;height:378px;background:var(--orange);font-family:"Roboto Condensed","Arial Narrow",sans-serif;color:var(--white)}
.f-title{position:absolute;font-weight:700;font-size:30px}
.f-line{position:absolute;font-size:20px;line-height:28px;white-space:nowrap}
</style>
</head>
<body>

<svg class="bg-art" width="1200" height="2400" viewBox="0 0 1200 2400" aria-hidden="true">
  <defs>
    <linearGradient id="heroGrad" x1="0" y1="0" x2="1" y2="1">
      <stop offset="0" stop-color="#007a80"/>
      <stop offset="0.6" stop-color="#00a3ad"/>
      <stop offset="1" stop-color="#1ec9d4"/>
    </linearGradient>
    <linearGradient id="trustGrad" x1="0" y1="0" x2="0" y2="1">
      <stop offset="0" stop-color="#007a80"/>
      <stop offset="1" stop-color="#00aab5"/>
    </linearGradient>
  </defs>
  <polygon points="37,0 1200,0 1200,461 494,461" fill="url(#heroGrad)"/>
  <line x1="0" y1="52" x2="1200" y2="52" stroke="#3fc1c9" stroke-width="1"/>
  <polygon points="0,1350 1200,1350 705,1812 0,1812" fill="url(#trustGrad)"/>
  <rect x="575" y="1233" width="22" height="2" fill="#f9a51a"/>
  <rect x="575" y="1238" width="22" height="2" fill="#f9a51a"/>
</svg>

<div class="art ribbon-area" role="img" aria-label="Decorative flowing blue ribbon behind the service cards"></div>

<div class="abs award" style="left:136px;top:9px">In 2020 Veldon Won Cyber Security<br>Excellence Award For Best Selling “Anti Phising”</div>
<div class="abs award" style="left:442px;top:9px">In 2020 Veldon Won Cyber Security<br>Excellence Award For Best “Security Education Platform”</div>
<div class="abs award" style="left:787px;top:9px">2020 Gold Winner ” Cyber Security<br>Education And Training”</div>
<div class="abs nav-btn nav-home" style="left:1037px;top:15px;width:46px;height:20px">Home</div>
<div class="abs nav-btn nav-solution" style="left:1097px;top:15px;width:62px;height:20px">Solution ▾</div>

<div class="art" role="img" aria-label="Photo of a smiling woman presenting with open hands" style="left:33px;top:75px;width:237px;height:386px;background:linear-gradient(180deg,#d9c1ad,#9ec3e6)"></div>
<div class="art" role="img" aria-label="Illustration of a desktop computer with floating app icons" style="left:438px;top:88px;width:284px;height:331px;background:linear-gradient(160deg,#4aa6d6,#1d3f66 55%,#b8c2cc);opacity:.85"></div>

<div class="abs hero-line" style="top:131px">CYBER SECURITY STARTS WITH PEOPLE</div>
<div class="abs hero-line" style="top:176px">TRAIN YOUR STAFF WITH VELDON AND IMPROVE<br>CYBER SECURITY AWARENESS</div>
<div class="abs demo-btn">Request A Demo</div>

<div class="dot" style="left:177px;top:473px;width:18px;height:18px;background:var(--teal)"></div>
<div class="dot" style="left:179px;top:507px;width:14px;height:14px;background:var(--teal-dark)"></div>
<div class="dot" style="left:180px;top:535px;width:12px;height:12px;background:var(--teal-deep)"></div>

<div class="art" role="img" aria-label="Security emblem illustration in orange and teal" style="left:524px;top:508px;width:140px;height:154px;background:linear-gradient(135deg,#f9c46b,#5fb7ba)"></div>

<div class="abs help-box">HOW CAN WE HELP ?</div>

<div class="card" style="left:35px;top:564px;height:389px">
  <div class="card-head">IMPORT OUR TRAINING<br>COURSES IN YOUR LMS</div>
  <p class="card-lead">Buy Out The Box Or Custom Tailored Security Courses You Can Import In Your Elearing (Scorm)</p>
  <p class="card-text">Veldon Offers 250 Fully Customizable Training Modules In +30 Languages Games, Videos, Exams, &nbsp;Posters, Offline, Micro- Training And Much More</p>
  <div class="card-btn" style="top:268px">EXPLORE OUR TRAINING</div>
</div>

<div class="card" style="left:433px;top:704px;height:388px">
  <div class="card-head">LET US DEVELOP A SECURITY<br>DEVELOPMENT PROGRAM</div>
  <p class="card-lead">Veldon Guard Will Assist You In Improving Security Awarenes With Money Back Guarantee</p>
  <p class="card-text">Our Security Awareness Specialists Will Identify Risk Users Via Phising Simulations We Develop A Tailored Awareness Program And Reduce Your Exposure To Social Hacking</p>
  <div class="card-btn" style="top:278px">EXPLORE OUR SERVICES</div>
</div>

<div class="card" style="left:831px;top:809px;height:389px">
  <div class="card-head left">INSTALL THE VELDON SOFTWARE ON PREMISE<br>OR GET ACCESS TO THE SAAS VERSION</div>
  <p class="card-lead">You Want To Run The Campaign Yourself? Choose Your Prefered Setup And Get Started In 24h</p>
  <p class="card-text">The Veldon Software Can Be Installed On Premise \Or in The Cloud . If You Dont Want Deal With The Installation We Onboard You In 24h on Our Saas</p>
  <div class="card-btn" style="top:283px">EXPLORE OUR SOFTWARE</div>
</div>

<div class="abs mssp">VELDON IS ALSO AVAILABLE FOR MSSP</div>
<div class="abs learn">Learn More</div>

<div class="abs trust-line" style="top:1372px;font-size:28px">Already Over 12’000’000 World Wide Trust And Use Veldon</div>
<div class="abs trust-line" style="top:1434px;left:59px">Veldon Guard Is A Name You Can Trust! Because We Have Won Countless<br>Awards Since @015 And Help Will- Known BRands Around The World</div>
<div class="abs trust-line" style="top:1532px">You Know You Are Geting A quality Solution With Us</div>
<div class="abs trust-line" style="top:1590px">Our Service Can Be Coustomized To Fit Your Needs And Company Size<br>Talk To Our Team Today to Learn More.</div>
<div class="abs contact-btn">GET IN CONTACT WITH VELDON TEAM NOW</div>

<div class="abs clients">
  <div class="client"><span class="mark"></span>Norvia</div>
  <div class="client">Helvara</div>
  <div class="client">Alpenflug</div>
  <div class="client">Kestrel</div>
  <div class="client">Tessin Informatik</div>
</div>

<div class="abs footer">
  <div class="f-title" style="left:106px;top:70px">CONTACTS</div>
  <div class="f-line" style="left:107px;top:124px">Address: Europe</div>
  <div class="f-line" style="left:105px;top:161px">Veldon Guard AG</div>
  <div class="f-line" style="left:103px;top:198px">Lindenweg 18 6301 Baar Switzerland</div>

  <div class="f-line" style="left:470px;top:72px">Address: North America</div>
  <div class="f-line" style="left:470px;top:109px">Veldon Guard USA</div>
  <div class="f-line" style="left:471px;top:149px">4820 Meridian Pkwy<br>Suit 210<br>Denver Co 80237</div>

  <div class="f-line" style="left:750px;top:72px">Phone Global: +41 44 310 28 46</div>
  <div class="f-line" style="left:750px;top:109px">Phone USA: +1 720 555 0148</div>
  <div class="f-line" style="left:750px;top:145px">Phone USA Support: +1 720 555 0148</div>
  <div class="f-line" style="left:750px;top:183px">Phone France: +33 6 55 01 2847</div>
  <div class="f-line" style="left:749px;top:222px">Phone UK: +44 (0) 7700 900461</div>

  <div class="f-title" style="left:107px;top:285px">LANGUAGE</div>
  <div class="f-line" style="left:109px;top:330px">English &nbsp;&nbsp;&nbsp;&nbsp;&nbsp;<span style="font-size:13px">▼</span></div>
</div>

</body>
</html>
```